Design some Business Cards for wedding photographers

My sister and I are wedding photographers. Our company is called MERIDIAN Wedding Photography. We need some business cards. Here is the information that needs to be on our card:

MERIDIAN Wedding Photography

[login to view URL]
[login to view URL]
merwedphoto@[login to view URL]
(555) 318-2946

We are going to use the same design for both of us but we would also like to have personalized cards. They can look the same but also have our names on it which are (we need individual cards obviously):

Vera Dalton
Marina Brooks

I am attaching our logo design. I also like the black background, it's also attached but we are open for different backgrounds as well.

Business cards should be two sided (the front and the back) and be standard size 3.5 x 2 in.

We would also like some sort of a sparkly effect on the ring.

I attached all the versions of the logo. You don't need all of them, you can just download the most appropriate format for you. The last two files is background.

```html
<!DOCTYPE html>
<html lang="en">
<head>
<meta charset="utf-8">
<title>MERIDIAN Wedding Photography – Business Cards</title>
<link href="https://fonts.googleapis.com/css2?family=Oswald:wght@300;400&family=Rokkitt:wght@400&display=swap" rel="stylesheet">
<style>
  :root {
    --backdrop: #dcdcd8;
    --card: #4a4a4a;
    --gold: #c9a862;
    --mint: #a9d9bd;
    --shadow: rgba(0, 0, 0, 0.22);
  }
  * { margin: 0; padding: 0; box-sizing: border-box; }
  html, body {
    width: 1200px;
    height: 777px;
    overflow: hidden;
    background: var(--backdrop);
  }
  .stage {
    position: relative;
    width: 1200px;
    height: 777px;
  }
  .card {
    position: absolute;
    top: 234px;
    width: 540px;
    height: 309px;
    background: var(--card);
    box-shadow: 0 6px 18px var(--shadow);
    overflow: hidden;
  }
  .card--front { left: 40px; }
  .card--back { left: 620px; }

  /* Front */
  .front-frame {
    position: absolute;
    left: 62px;
    top: 46px;
    right: 62px;
    bottom: 46px;
    border: 3px solid var(--gold);
    display: flex;
    flex-direction: column;
    align-items: center;
    justify-content: center;
  }
  .brand {
    display: flex;
    align-items: center;
    gap: 10px;
  }
  .brand-name {
    font-family: "Oswald", sans-serif;
    font-weight: 400;
    font-size: 50px;
    letter-spacing: 3px;
    color: var(--mint);
    line-height: 1;
  }
  .brand-dot {
    width: 14px;
    height: 14px;
    border-radius: 50%;
    background: var(--gold);
    margin-top: -26px;
  }
  .brand-tagline {
    font-family: "Oswald", sans-serif;
    font-weight: 300;
    font-size: 22px;
    color: var(--gold);
    margin-top: 6px;
    letter-spacing: 0.5px;
  }

  /* Back */
  .name-frame {
    position: absolute;
    left: 268px;
    top: 58px;
    width: 226px;
    height: 118px;
    border: 3px solid var(--gold);
    transform: rotate(-17deg);
    display: flex;
    align-items: center;
    justify-content: center;
  }
  .holder-name {
    font-family: "Rokkitt", serif;
    font-size: 31px;
    color: var(--gold);
    white-space: nowrap;
  }
  .contact {
    position: absolute;
    left: 34px;
    bottom: 30px;
    font-family: "Oswald", sans-serif;
    font-weight: 300;
    color: var(--mint);
    line-height: 1.25;
  }
  .contact-phone { font-size: 22px; letter-spacing: 3px; margin-bottom: 4px; }
  .contact-email { font-size: 16px; }
  .contact-web { font-size: 25px; font-weight: 400; }
  .contact-social { font-size: 16px; }
</style>
</head>
<body>
<main class="stage">
  <section class="card card--front" aria-label="Card front">
    <div class="front-frame">
      <div class="brand">
        <span class="brand-name">MERIDIAN</span>
        <span class="brand-dot"></span>
      </div>
      <div class="brand-tagline">wedding photography</div>
    </div>
  </section>

  <section class="card card--back" aria-label="Card back">
    <div class="name-frame">
      <span class="holder-name">Marina Brooks</span>
    </div>
    <div class="contact">
      <div class="contact-phone">(555) 318-2946</div>
      <div class="contact-email">merwedphoto@postmail.com</div>
      <div class="contact-web">merwedphoto.com</div>
      <div class="contact-social">pagebook.com/merwedphoto</div>
    </div>
  </section>
</main>
</body>
</html>
```